" Empresa focada em seguros pessoais, tais como seguro saúde, vida, previdência e odontológico, oferecendo segurança e agilidade na contrataçao e manutençao e também qualidade de vida. "

```html
<!DOCTYPE html>
<html lang="pt-BR">
<head>
<meta charset="UTF-8">
<title>Litoral – Cartões de visita</title>
<link rel="stylesheet" href="https://fonts.googleapis.com/css2?family=Arimo:wght@400&display=swap">
<style>
  :root {
    --navy: #1a2456;
    --white: #ffffff;
    --paper: #fbfbfd;
    --backdrop: #e6e6e8;
    --muted: #4a5280;
  }
  * { margin: 0; padding: 0; box-sizing: border-box; }
  html, body {
    width: 1200px;
    height: 1200px;
    overflow: hidden;
    background: var(--backdrop);
  }
  .canvas {
    position: relative;
    width: 1200px;
    height: 1200px;
    font-family: "Arimo", sans-serif;
    font-weight: 400;
  }
  .card {
    position: absolute;
    left: 210px;
    width: 780px;
    height: 433px;
    border-radius: 4px;
    box-shadow: 0 18px 40px rgba(0,0,0,0.18);
    overflow: hidden;
  }
  .card--back { top: 140px; background: var(--paper); }
  .card--front { top: 627px; background: var(--navy); }

  .brand-name { line-height: 1; letter-spacing: 1px; }
  .brand-tagline { letter-spacing: 0.5px; margin-top: 8px; }

  /* back card */
  .back-brand {
    position: absolute;
    left: 70px;
    top: 250px;
    color: var(--navy);
  }
  .back-brand .brand-name { font-size: 46px; }
  .back-brand .brand-tagline { font-size: 17px; }

  .contact {
    position: absolute;
    left: 470px;
    top: 70px;
    color: var(--navy);
    font-size: 14px;
    line-height: 1.45;
  }
  .contact__name { font-size: 17px; margin-bottom: 22px; }
  .contact__address { margin-top: 48px; font-size: 12px; color: var(--muted); }

  /* front card */
  .front-brand {
    position: absolute;
    left: 250px;
    top: 130px;
    color: var(--white);
    display: flex;
    align-items: center;
    gap: 20px;
  }
  .front-brand__dot {
    width: 30px;
    height: 30px;
    border-radius: 50%;
    background: var(--white);
    flex: none;
  }
  .front-brand .brand-name { font-size: 56px; }
  .front-brand .brand-tagline { font-size: 19px; }

  .website {
    position: absolute;
    left: 0;
    right: 0;
    bottom: 58px;
    text-align: center;
    font-size: 14px;
    letter-spacing: 6px;
    color: var(--white);
  }
</style>
</head>
<body>
<main class="canvas">

  <section class="card card--back" aria-label="Verso do cartão">
    <div class="back-brand">
      <div class="brand-name">Litoral</div>
      <div class="brand-tagline">Seguros e Benefícios</div>
    </div>
    <div class="contact">
      <p class="contact__name">Marina Duarte</p>
      <p>contato@litoralseguros.com.br</p>
      <p>(48) 3024-1180</p>
      <p>(48) 99812-4470</p>
      <div class="contact__address">
        <p>Av. das Gaivotas, 1280</p>
        <p>Florianópolis - SC</p>
        <p>CEP 88010-000</p>
      </div>
    </div>
  </section>

  <section class="card card--front" aria-label="Frente do cartão">
    <div class="front-brand">
      <div class="front-brand__dot" aria-hidden="true"></div>
      <div>
        <div class="brand-name">Litoral</div>
        <div class="brand-tagline">Seguros e Benefícios</div>
      </div>
    </div>
    <p class="website">www.litoralseguros.com.br</p>
  </section>

</main>
</body>
</html>
```